Nur Briefpapier und VK für Pflegedienst, Logo vorhanden!!!!
Zielgruppe
Wir sind ein Pflegedienst, unsere Zielgruppe sind Krankenkassen und Patienten und andere Krankenhäuser mit denen wir zusammen arbeiten.
Aufgabenstellung
modern, seriös, elitär

```html
<!DOCTYPE html>
<html lang="de">
<head>
<meta charset="utf-8">
<title>Renofleet Pflegedienst – Geschäftsausstattung</title>
<link href="https://fonts.googleapis.com/css2?family=Ubuntu:wght@300;400;500;700&display=swap" rel="stylesheet">
<style>
  :root {
    --brand-red: #9b1b1d;
    --band-start: #e8232f;
    --band-mid: #e20b1a;
    --band-end: #8f1a1a;
    --ink: #2b2b2b;
    --ink-soft: #555;
    --paper: #ffffff;
    --edge: #8c8c8c;
    --shadow: rgba(0,0,0,0.35);
  }
  * { box-sizing: border-box; margin: 0; padding: 0; }
  html, body { width: 1200px; height: 1200px; overflow: hidden; background: #fff; }
  body { position: relative; font-family: "Ubuntu", sans-serif; color: var(--ink); }

  .sheet {
    position: absolute;
    background: var(--paper);
    border: 1px solid var(--edge);
    box-shadow: 5px 6px 6px var(--shadow);
    overflow: hidden;
  }
  .band {
    position: absolute; left: 0; right: 0; bottom: 0;
    background: linear-gradient(90deg, var(--band-start) 0%, var(--band-mid) 35%, var(--band-end) 100%);
    color: #fff;
  }

  .wordmark {
    position: absolute;
    display: flex; align-items: center; justify-content: center; gap: 0.3em;
    color: var(--brand-red);
    font-weight: 700;
    white-space: nowrap;
  }
  .wordmark .mark-square {
    width: 0.55em; height: 0.55em; background: var(--brand-red);
  }

  /* business card front */
  .card-front { left: 366px; top: 61px; width: 270px; height: 175px; z-index: 2; }
  .card-front .name { position: absolute; left: 23px; top: 20px; font-size: 9.4px; font-weight: 700; color: var(--brand-red); }
  .card-front .role { position: absolute; left: 23px; top: 34px; font-size: 7.2px; font-weight: 300; color: var(--ink-soft); }
  .contact-list { position: absolute; left: 23px; top: 58px; list-style: none; font-size: 7.2px; font-weight: 300; color: var(--ink-soft); }
  .contact-list li { display: flex; align-items: center; gap: 4px; height: 12.4px; }
  .contact-list svg { width: 7px; height: 7px; flex: none; }
  .card-front .wordmark { left: 196px; top: 42px; width: 70px; font-size: 10px; }
  .card-front .band { height: 58px; font-size: 6.3px; }
  .card-front .company { position: absolute; left: 23px; top: 18px; font-weight: 700; }
  .card-front .address { position: absolute; left: 23px; top: 29px; font-weight: 300; }
  .card-front .web { position: absolute; right: 22px; top: 29px; font-weight: 700; }

  /* business card back */
  .card-back { left: 571px; top: 96px; width: 270px; height: 175px; z-index: 1; }
  .card-back .wordmark { left: 70px; top: 76px; width: 130px; font-size: 15px; }

  /* letterhead */
  .letter { left: 115px; top: 354px; width: 534px; height: 754px; z-index: 2; }
  .letter .wordmark { left: 400px; top: 100px; width: 110px; font-size: 14px; }
  .sender-line { position: absolute; left: 50px; top: 112px; font-size: 5.6px; color: var(--ink-soft); display: flex; align-items: center; gap: 4px; }
  .sender-line .dot { width: 3px; height: 3px; background: var(--brand-red); }
  .fold-mark { position: absolute; left: 0; height: 1px; background: #333; }
  .letter-body { position: absolute; left: 50px; top: 264px; width: 428px; font-size: 8.4px; line-height: 13.4px; color: var(--ink); }
  .letter-body p { margin-bottom: 13.4px; }
  .letter-body .signature { margin-top: 40px; }
  .letter .band { height: 71px; font-size: 6.1px; line-height: 10.6px; }
  .footer-col { position: absolute; top: 18px; }

  /* letterhead back */
  .letter-back { left: 559px; top: 392px; width: 534px; height: 754px; z-index: 1; border-color: #aaa; box-shadow: 4px 5px 6px rgba(0,0,0,0.18); }
  .letter-back .wordmark { left: 167px; top: 333px; width: 200px; font-size: 24px; }
</style>
</head>
<body>

  <section class="sheet card-back" aria-label="Visitenkarte Rückseite">
    <div class="wordmark"><span class="mark-square"></span>Renofleet</div>
  </section>

  <section class="sheet card-front" aria-label="Visitenkarte Vorderseite">
    <div class="name">Jonas Beispielmann</div>
    <div class="role">Geschäftsführer</div>
    <ul class="contact-list">
      <li><svg viewBox="0 0 10 10"><rect width="10" height="10" rx="1" fill="#9b1b1d"/><path d="M3 2.2c.4 2.6 2 4.3 4.8 5.3l.6-1.3-1.4-.8-.7.7C5.2 5.6 4.5 4.8 4.2 3.8l.7-.6-.7-1.5z" fill="#fff"/></svg>030 41 27 65 18</li>
      <li><svg viewBox="0 0 10 10"><rect width="10" height="10" rx="1" fill="#9b1b1d"/><rect x="2.5" y="1.8" width="5" height="2.5" fill="#fff"/><rect x="1.8" y="4.6" width="6.4" height="3.6" fill="none" stroke="#fff" stroke-width="0.9"/></svg>030 41 27 65 19</li>
      <li><svg viewBox="0 0 10 10"><rect width="10" height="10" rx="1" fill="#9b1b1d"/><rect x="1.8" y="2.8" width="6.4" height="4.4" fill="#fff"/><path d="M1.8 2.8L5 5.6l3.2-2.8" fill="none" stroke="#9b1b1d" stroke-width="0.8"/></svg>j.beispielmann@renofleet-pflege.de</li>
    </ul>
    <div class="wordmark"><span class="mark-square"></span>Renofleet</div>
    <div class="band">
      <div class="company">Renofleet Pflegedienst</div>
      <div class="address">Lindenallee 45 • 37412 Talbrück</div>
      <div class="web">www.renofleet-pflege.de</div>
    </div>
  </section>

  <section class="sheet letter-back" aria-label="Briefbogen Rückseite">
    <div class="wordmark"><span class="mark-square"></span>Renofleet</div>
  </section>

  <section class="sheet letter" aria-label="Briefbogen">
    <div class="wordmark"><span class="mark-square"></span>Renofleet</div>
    <div class="sender-line">
      <span>Renofleet Pflegedienst</span><span class="dot"></span>
      <span>Lindenallee 45</span><span class="dot"></span>
      <span>37412 Talbrück</span>
    </div>

    <span class="fold-mark" style="top:266px;width:15px"></span>
    <span class="fold-mark" style="top:376px;width:25px"></span>
    <span class="fold-mark" style="top:533px;width:15px"></span>

    <div class="letter-body">
      <p>Sehr geeherter Herr Beispielmann,</p>
      <p>Nam essenisquas sapere doluptam voluptam, idit et, vent, erferor rorpos reste liberi qui omnis vellupt atibus, omnihiciti quamus untionse necerov itibus cusdanda nihiliquo velitatia aliquidit velis ut od es aut aperum quatemo luptur.</p>
      <p>Am etus dolupta nes molore, te moditatibus, ipsunt porionem re volutem olupta dem qui dellit odit ut eaqui odigenis sed quasit et reptatem inienda provita tiumque et ea quis solum alique viducia non repelit fugia de escid ut ant exeruptis que suntis untionsectia int as quisimpor maionem postiorerum quiae nonse ne simi, consequi ius nonectation cusda quas volupici dis duciis et od etur, acid ut aut officiatusae pa volorrum intibeature, sincipsam venis acipsam quaspero beriorem rempost, que venisit eatiosamusa nobit vellat quati reius.</p>
      <p>Dellore pelitatur? Catem qui im volorerem quodi simint eaquid que quassed maximin venducit qui deliquatum exceperspe am, cuscidi tiossendae ad et eum cum debit, simposs invellu ptatque poriore sequia ditatemposae nis mod quo test, ius vent etur, ommodip suntempor arupta debit estibus cienimus plab illiquis dolupta non pratibe rcidus eaquia incimoluptat quamet hillandamus modis quia velignihilit perum quam liquas eaquam que pore eumqui doluptat.</p>
      <p>Mit&nbsp; freundlichen Grüßen,</p>
      <p class="signature">Jonas Beispielmann</p>
    </div>

    <footer class="band">
      <div class="footer-col" style="left:50px">renofleet-pflege<br>Geschäftsführende Gesellschafter:<br>Jonas Beispielmann</div>
      <div class="footer-col" style="left:191px">Hauptverwaltung Talbrück<br>Amtsgericht Talbrück, HRB4821<br>USt-IdNr. DE 284617359</div>
      <div class="footer-col" style="left:317px">Lindenallee 45<br>37412 Talbrück</div>
      <div class="footer-col" style="left:415px">T. 030 41 27 65 18<br>F. 030 41 27 65 19<br>info@renofleet-pflege.de</div>
    </footer>
  </section>

</body>
</html>
```